BRIM Outreach Partners Business Card Rebrand

Hello Designers! We are looking for help designing our new business card to go in conjunction with our company rebrand. Unfortunately, we have an event mid June that requires we get these printed ASAP (before our new website is launched.) We have a mostly complete Brand Book which I have uploaded to this request for your reference to company information, style, fonts. I've also enclosed our logo file in .eps & .jpg. Attached is a sample business card my boss liked but said was "too simple." I made it in Canva and do not profess to be a designer. NOT FOR DESIGN REFERENCE, ONLY FOR CONTEXT Here is what our old website looks like: https://brimoutreachpartners.com/.

```html
<!DOCTYPE html>
<html lang="en">
<head>
<meta charset="utf-8">
<title>BRIM Outreach Partners – Business Card</title>
<link rel="stylesheet" href="https://fonts.googleapis.com/css2?family=Poppins:wght@400;600;700&display=swap">
<style>
  :root {
    --page-bg: #e9e9ea;
    --ink-dark: #2b2b2d;
    --brand-blue: #5db4e5;
    --card-white: #ffffff;
    --text-muted: #3a3a3c;
    --rule: #4a4a4c;
  }
  * { box-sizing: border-box; margin: 0; padding: 0; }
  html, body {
    width: 1200px; height: 900px; overflow: hidden;
    background: var(--page-bg);
    font-family: "Poppins", sans-serif;
  }
  .card-set {
    position: absolute; left: 320px; top: 100px;
    display: flex; flex-direction: column; gap: 60px;
  }
  .card {
    position: relative; width: 560px; height: 320px; overflow: hidden;
    box-shadow: 0 8px 20px rgba(0,0,0,0.12);
  }
  /* Front */
  .card-front { background: var(--ink-dark); display: flex; align-items: center; justify-content: center; }
  .brand-lockup { display: flex; align-items: center; gap: 16px; }
  .brand-dot { width: 64px; height: 64px; border-radius: 50%; background: var(--brand-blue); flex: none; }
  .brand-name { font-weight: 600; font-size: 30px; line-height: 1.1; }
  .card-front .brand-name { color: var(--card-white); }
  /* Back */
  .card-back { background: var(--card-white); }
  .card-back .brand-lockup { position: absolute; left: 140px; top: 44px; }
  .card-back .brand-dot { width: 52px; height: 52px; }
  .card-back .brand-name { color: var(--ink-dark); font-size: 26px; }
  .person { position: absolute; left: 40px; top: 170px; width: 220px; }
  .person-name { color: var(--brand-blue); font-weight: 700; font-size: 18px; letter-spacing: 0.5px; text-transform: uppercase; }
  .person-role { color: var(--text-muted); font-size: 14px; margin-top: 2px; }
  .divider { position: absolute; left: 272px; top: 140px; width: 1px; height: 110px; background: var(--rule); }
  .contact-list { position: absolute; left: 290px; top: 138px; list-style: none; font-size: 12px; color: var(--text-muted); }
  .contact-list li { display: flex; align-items: center; gap: 8px; line-height: 24px; }
  .contact-list .location { padding-left: 0; margin-bottom: 2px; }
  .contact-icon { width: 12px; height: 12px; flex: none; }
  .edge-bands { position: absolute; left: 0; bottom: 0; }
</style>
</head>
<body>
  <main class="card-set">
    <section class="card card-front" aria-label="Card front">
      <div class="brand-lockup">
        <span class="brand-dot"></span>
        <span class="brand-name">BRIM Outreach Partners</span>
      </div>
    </section>

    <section class="card card-back" aria-label="Card back">
      <div class="brand-lockup">
        <span class="brand-dot"></span>
        <span class="brand-name">BRIM Outreach Partners</span>
      </div>

      <div class="person">
        <p class="person-name">Daniel Marsh-Tolley</p>
        <p class="person-role">Managing Partner</p>
      </div>

      <span class="divider"></span>

      <ul class="contact-list">
        <li class="location">Atlanta, GA based (Central Time)</li>
        <li>
          <svg class="contact-icon" viewBox="0 0 12 12" aria-hidden="true"><path d="M2 1h3l1 3-1.5 1a7 7 0 0 0 2.5 2.5L8 6l3 1v3a1 1 0 0 1-1 1A9 9 0 0 1 1 2a1 1 0 0 1 1-1z" fill="var(--brand-blue)"/></svg>
          +945-555-0142
        </li>
        <li>
          <svg class="contact-icon" viewBox="0 0 12 12" aria-hidden="true"><rect x="0.5" y="2" width="11" height="8" rx="1" fill="var(--brand-blue)"/><path d="M1 3l5 3.5L11 3" stroke="#fff" stroke-width="1" fill="none"/></svg>
          daniel@brimoutreachpartners.com
        </li>
        <li>
          <svg class="contact-icon" viewBox="0 0 12 12" aria-hidden="true"><circle cx="6" cy="6" r="5.5" fill="var(--brand-blue)"/><path d="M0.5 6h11M6 0.5c-2.5 3-2.5 8 0 11M6 0.5c2.5 3 2.5 8 0 11" stroke="#fff" stroke-width="0.8" fill="none"/></svg>
          www.brimoutreachpartners.com
        </li>
      </ul>

      <svg class="edge-bands" width="560" height="40" viewBox="0 0 560 40" aria-hidden="true">
        <polygon points="0,30 382,30 392,18 402,18 388,40 0,40" fill="var(--brand-blue)"/>
        <polygon points="402,18 560,18 560,40 388,40" fill="var(--ink-dark)"/>
      </svg>
    </section>
  </main>
</body>
</html>
```